Business Card for Consulting Company

I would need a business card for my consulting company - the company brand and logos are defined and shared as part of this project. The proposed design for the business card can be reused as inspiration for my email signature.

```html
<!DOCTYPE html>
<html lang="en">
<head>
<meta charset="utf-8">
<title>Meridian Axis – Business Card</title>
<link rel="stylesheet" href="https://fonts.googleapis.com/css2?family=Lato:wght@400;700&family=Montserrat:wght@600;700&display=swap">
<style>
  :root {
    --teal: #18a9a9;
    --teal-soft: #6fcaca;
    --ink: #3d3d3f;
    --paper: #ffffff;
    --stage: #e9ebec;
    --rule: #55585b;
  }
  * { margin: 0; padding: 0; box-sizing: border-box; }
  html, body { width: 1200px; height: 895px; overflow: hidden; }
  body {
    background: var(--stage);
    font-family: "Lato", sans-serif;
    position: relative;
  }
  .card {
    position: absolute;
    width: 520px;
    height: 336px;
    border-radius: 3px;
    box-shadow: 0 12px 30px rgba(0,0,0,0.18);
    overflow: hidden;
  }
  /* Front */
  .card--front {
    left: 60px; top: 70px;
    background: var(--teal);
    display: flex; flex-direction: column; align-items: center;
  }
  .brand {
    display: flex; align-items: center; gap: 10px;
    font-family: "Montserrat", sans-serif;
    font-weight: 700;
    white-space: nowrap;
    line-height: 1;
  }
  .brand__dot { border-radius: 50%; flex: none; }
  .card--front .brand { margin-top: 124px; font-size: 38px; color: var(--teal-soft); }
  .card--front .brand__dot { width: 22px; height: 22px; background: var(--teal-soft); }
  .front__url {
    margin-top: 96px;
    color: var(--paper);
    font-weight: 700;
    font-size: 15px;
    letter-spacing: 1.2px;
  }
  /* Back */
  .card--back {
    left: 620px; top: 489px;
    background: var(--paper);
  }
  .card--back .brand {
    position: absolute; left: 28px; top: 190px;
    font-size: 25px; color: var(--teal);
  }
  .card--back .brand__dot { width: 15px; height: 15px; background: var(--teal); }
  .back__rule {
    position: absolute; left: 262px; top: 118px;
    width: 1px; height: 150px; background: var(--rule);
  }
  .contact { position: absolute; left: 286px; top: 108px; }
  .contact__name {
    font-family: "Montserrat", sans-serif;
    font-weight: 700; font-size: 25px; color: var(--ink);
    line-height: 1;
    white-space: nowrap;
  }
  .contact__name-first { color: var(--teal); }
  .contact__role { font-size: 15px; color: var(--ink); margin-top: 6px; }
  .contact__list { list-style: none; margin-top: 18px; }
  .contact__item {
    display: flex; align-items: center; gap: 10px;
    font-size: 14px; color: var(--ink); line-height: 22px;
    white-space: nowrap;
  }
  .contact__icon { width: 14px; height: 14px; flex: none; }
</style>
</head>
<body>
  <section class="card card--front" aria-label="Card front">
    <div class="brand"><span class="brand__dot"></span>Meridian Axis</div>
    <p class="front__url">www.meridianaxis.ch</p>
  </section>

  <section class="card card--back" aria-label="Card back">
    <div class="brand"><span class="brand__dot"></span>Meridian Axis</div>
    <div class="back__rule"></div>
    <div class="contact">
      <h1 class="contact__name"><span class="contact__name-first">Lucien</span> Moreau</h1>
      <p class="contact__role">Founder &amp; CEO</p>
      <ul class="contact__list">
        <li class="contact__item">
          <svg class="contact__icon" viewBox="0 0 24 24" fill="#18a9a9"><path d="M6.6 10.8a15.1 15.1 0 0 0 6.6 6.6l2.2-2.2c.3-.3.7-.4 1-.2 1.1.4 2.3.6 3.6.6.6 0 1 .4 1 1V20c0 .6-.4 1-1 1A17 17 0 0 1 3 4c0-.6.4-1 1-1h3.5c.6 0 1 .4 1 1 0 1.3.2 2.5.6 3.6.1.3 0 .7-.2 1z"/></svg>
          +41 79 482 17 36
        </li>
        <li class="contact__item">
          <svg class="contact__icon" viewBox="0 0 24 24" fill="none" stroke="#18a9a9" stroke-width="2"><rect x="3" y="5" width="18" height="14" rx="1"/><path d="M3 6l9 7 9-7"/></svg>
          lucien.m@meridianaxis.ch
        </li>
        <li class="contact__item">
          <svg class="contact__icon" viewBox="0 0 24 24" fill="none" stroke="#18a9a9" stroke-width="2"><circle cx="12" cy="12" r="9"/><path d="M3 12h18M12 3c3 3 3 15 0 18M12 3c-3 3-3 15 0 18"/></svg>
          www.meridianaxis.ch
        </li>
      </ul>
    </div>
  </section>
</body>
</html>
```